Pregnancy and Fertility Information Website

Hello Designers,
I need a website which provide tips and information about healthy and happy pregnancy. My website name is KRE medical.

The website should provide all the information needed throughout pregnancy and beyond ranging from pregnancy tracking tools and articles about common pregnancy concerns and what to expect during pregnancy,etc.
The details about first trimester, second trimester and third trimester should be highlighted in the website.

Top Navigation
Home, Fertility, Pregnancy basics, Articles, Tips and News

I'm looking for a simple and clean design which involves captivating images and colors but it shouldn't be crowded. The design must be professional and modern. An easy to navigate layout is a must.

Green, violet, blue and light yellow colors are my favorites but i'm open to other options.

Any questions. Kindly ask

Industry/Entity Type

Medical

```html
<!DOCTYPE html>
<html lang="en">
<head>
<meta charset="utf-8">
<title>KRE Medical – Pregnancy &amp; Fertility</title>
<link rel="stylesheet" href="https://fonts.googleapis.com/css2?family=Marcellus&family=Lato:wght@400;700&display=swap">
<style>
:root{
  --blue:#1d6fb8;
  --blue-dark:#15579a;
  --green:#5aac44;
  --green-light:#6cbf55;
  --ink:#333;
  --muted:#555;
  --footer:#0f1a24;
  --footer-line:#2a3642;
  --footer-text:#e6ebf0;
  --rule:#e3e3e3;
}
*{box-sizing:border-box;margin:0;padding:0}
html,body{width:1200px;height:3315px;overflow:hidden}
body{position:relative;background:#fff;font-family:"Lato",sans-serif;color:var(--ink);font-size:14px}
.abs{position:absolute}

/* top bar */
.topbar{left:0;top:0;width:1200px;height:48px;background:var(--blue);color:#fff;font-size:13px}
.topbar .mail{left:100px;top:15px}
.topbar .support{right:100px;top:15px}
.icon{display:inline-block;vertical-align:middle;margin-right:8px}

/* header */
.header{left:0;top:48px;width:1200px;height:92px;background:#fff}
.logo-plate{left:520px;top:0;width:160px;height:150px;background:#fff;clip-path:polygon(0 0,100% 0,100% 70%,50% 100%,0 70%);}
.brand{left:520px;top:52px;width:160px;text-align:center}
.brand .dot{width:34px;height:34px;border-radius:50%;background:var(--green);margin:0 auto 6px}
.brand .name{font-family:"Lato",sans-serif;font-weight:700;font-size:22px;color:var(--blue);letter-spacing:1px}
.nav{font-family:"Marcellus",serif;font-size:14px;color:#333;text-transform:uppercase}
.nav a{position:absolute;color:inherit;text-decoration:none;white-space:nowrap}
.nav .sep{position:absolute;width:1px;height:26px;background:var(--rule);top:-5px}
.nav .active{background:var(--green);color:#fff;padding:13px 18px;top:-13px}
.search{left:1055px;top:70px;width:44px;height:44px;border-radius:50%;background:#222}

/* hero */
.hero{left:0;top:140px;width:1200px;height:560px;background:linear-gradient(90deg,#e7e6e3 0%,#f3f2ef 45%,#d9d2cb 75%,#ece8e3 100%)}
.hero-title{left:100px;top:372px;font-family:"Marcellus",serif;font-weight:400;font-size:36px;color:var(--blue)}
.hero-text{left:100px;top:420px;width:420px;font-size:13px;line-height:1.5;color:var(--muted)}
.dots{left:560px;top:650px}
.dots span{display:inline-block;width:12px;height:12px;border-radius:50%;border:2px solid #555;margin:0 2px}
.dots span.on{background:#3a6ea5;border-color:#3a6ea5}

/* section headings */
.heading{width:1200px;left:0;text-align:center;font-family:"Marcellus",serif;font-size:30px;font-weight:400;color:var(--blue)}
.heading em,.col-head em{font-style:normal;color:var(--green)}
.divider{left:580px}
.intro{left:100px;width:1000px;text-align:center;font-size:13px;line-height:1.9;color:#444}

/* trimesters */
.tri-photo{top:913px;width:316px;height:247px;border:5px solid var(--blue);box-shadow:0 10px 10px -6px rgba(0,0,0,.25)}
.tri-title{top:1190px;width:316px;text-align:center;font-family:"Marcellus",serif;font-size:20px;color:var(--blue)}
.btn{display:inline-flex;align-items:center;gap:10px;background:var(--blue);color:#fff;font-size:12px;font-weight:700;border-radius:16px;padding:0 5px 0 18px;height:32px}
.btn .arr{width:24px;height:24px;border-radius:50%;background:#fff;display:flex;align-items:center;justify-content:center}
.btn.ghost{background:rgba(255,255,255,.1);border:2px solid #fff;color:#fff}
.tri-btn{top:1237px}

/* fertility band */
.band{top:1320px;height:364px;width:600px}
.band.left{left:0;background:linear-gradient(135deg,#1c6db8,#3e8fcf)}
.band.right{left:600px;background:linear-gradient(135deg,#5cb14a,#8ccc6f)}
.band h3{position:absolute;top:55px;font-family:"Marcellus",serif;font-size:26px;font-weight:400;color:#fff}
.band p{position:absolute;top:120px;width:370px;font-size:13px;line-height:1.9;color:#fff;text-align:justify}
.band .btn{position:absolute;top:275px}
.hub{left:490px;top:1392px;width:220px;height:220px;border-radius:50%;background:#fff;border:8px solid rgba(255,255,255,.55);box-shadow:0 0 0 10px rgba(255,255,255,.25)}
.hub .brand{position:static;width:auto;margin-top:70px}

/* articles */
.articles-bg{left:0;top:1900px;width:1200px;height:460px;background:linear-gradient(180deg,#fff 0%,#f1f2f4 30%,#f7f7f8 100%)}
.thumb{width:120px;height:120px;border-radius:50%;top:1898px;border:3px solid #fff;box-shadow:0 2px 6px rgba(0,0,0,.15)}
.thumb.sel{width:160px;height:160px;top:1878px;border:8px solid var(--blue)}
.pin{left:310px;top:2035px;width:0;height:0;border-left:14px solid transparent;border-right:14px solid transparent;border-top:18px solid var(--blue)}
.art-photo{left:100px;top:2090px;width:212px;height:248px;background:linear-gradient(135deg,#c9a791,#eee7df 60%,#d8c3b3)}
.social-dot{left:342px;width:36px;height:36px;border-radius:50%;border:2px solid var(--blue);background:#fff}
.vline{left:359px;width:2px;background:var(--blue)}
.art{left:409px;top:2100px;width:692px}
.art h4{font-family:"Marcellus",serif;font-size:20px;font-weight:400;color:var(--blue);margin-bottom:14px}
.art .meta{font-size:14px;font-weight:700;margin-bottom:12px}
.art .meta span{margin:0 18px;color:#999}
.art p{font-size:13px;line-height:1.9;text-align:justify;color:#444}
.chev{top:1945px}

/* tips & news */
.col-head{top:2435px;font-family:"Marcellus",serif;font-size:27px;font-weight:400;color:var(--blue)}
.col-rule{top:2482px;height:1px;background:var(--rule)}
.navc{width:26px;height:26px;border-radius:50%;border:2px solid #888;top:2440px;display:flex;align-items:center;justify-content:center}
.navc.on{border-color:var(--blue)}
.item-title{font-family:"Marcellus",serif;font-size:14px;color:var(--blue)}
.item-text{font-size:13px;line-height:1.7;color:#444}
.item-date{font-size:12px;color:#444}
.tip-photo{width:128px;height:88px;background:linear-gradient(135deg,#e8e4e0,#c7cfd9)}
.datebox{width:50px;height:76px;text-align:center;color:#fff}
.datebox .d{background:var(--blue);height:40px;font-family:"Marcellus",serif;font-size:24px;line-height:40px}
.datebox .m{background:var(--green);height:36px;font-size:10px;line-height:1.4;padding-top:4px}
.vsep{left:600px;top:2440px;width:1px;height:290px;background:var(--rule)}

/* footer */
.footer{left:0;top:2773px;width:1200px;height:542px;background:var(--footer);color:#fff}
.fnav{top:2815px;left:0;width:1200px;font-family:"Marcellus",serif;font-size:16px;color:#fff}
.fnav a{position:absolute;color:#fff;text-decoration:none;text-transform:uppercase}
.fnav .sep{position:absolute;width:1px;height:20px;background:#5a6470;top:0}
.frule{left:100px;top:2868px;width:1000px;height:1px;background:var(--footer-line)}
.fhead{top:2910px;font-family:"Marcellus",serif;font-size:20px;font-weight:400;color:#fff}
.field{left:100px;width:320px;height:34px;border:1px solid #7e8a96;border-radius:17px;padding:0 18px;font-size:13px;line-height:32px;color:#fff}
.field.msg{height:62px;border-radius:22px}
.submit{left:100px;top:3166px}
.fcontact{left:778px;width:330px;color:var(--footer-text)}
.fcontact .ic{position:absolute;left:0;width:30px;height:30px;border-radius:50%;border:1px solid #7e8a96;display:flex;align-items:center;justify-content:center}
.fcontact .t{position:absolute;left:48px;width:280px;font-size:13px;line-height:1.5;color:var(--footer-text)}
.fcontact .t b{display:block;font-size:13px;font-weight:700;color:#fff}
.sq{top:3158px;width:22px;height:22px}
.copy{top:3268px;left:0;width:1200px;text-align:center;font-size:13px;color:#cfd6dd}
.flogo{left:470px;top:2960px;width:260px;height:210px}
.flogo .dot{width:44px;height:44px;border-radius:50%;background:var(--green);margin:40px auto 10px}
.flogo .name{font-weight:700;font-size:30px;color:var(--blue);text-align:center;letter-spacing:1px}
.map{left:760px;top:2890px;width:420px;height:300px;background:radial-gradient(ellipse at center,rgba(255,255,255,.05),rgba(255,255,255,0) 70%)}
</style>
</head>
<body>

<!-- top bar -->
<div class="abs topbar">
  <div class="abs mail"><svg class="icon" width="14" height="11" viewBox="0 0 14 11"><rect x="0.5" y="0.5" width="13" height="10" fill="#fff"/><path d="M1 1l6 5 6-5" stroke="#1d6fb8" fill="none"/></svg>info@kremedical.com</div>
  <div class="abs support"><svg class="icon" width="14" height="14" viewBox="0 0 24 24"><path fill="#fff" d="M6.6 10.8a15 15 0 006.6 6.6l2.2-2.2c.3-.3.7-.4 1-.2 1.1.4 2.3.6 3.6.6.6 0 1 .4 1 1V20c0 .6-.4 1-1 1A17 17 0 013 4c0-.6.4-1 1-1h3.5c.6 0 1 .4 1 1 0 1.3.2 2.5.6 3.6.1.3 0 .7-.2 1z"/></svg>Need Support? 123-456-7890</div>
</div>

<!-- header -->
<header class="abs header">
  <nav class="abs nav" style="left:0;top:24px;width:1200px">
    <a class="active" style="left:100px">Home</a>
    <span class="sep" style="left:184px"></span>
    <a style="left:200px">Fertility</a>
    <span class="sep" style="left:295px"></span>
    <a style="left:315px">Pregnancy Basics</a>
    <span class="sep" style="left:480px"></span>
    <span class="sep" style="left:725px"></span>
    <a style="left:755px">Articles</a>
    <span class="sep" style="left:850px"></span>
    <a style="left:880px">Tips</a>
    <span class="sep" style="left:940px"></span>
    <a style="left:968px">News</a>
  </nav>
</header>
<div class="abs logo-plate"></div>
<div class="abs brand"><div class="dot"></div><div class="name">KRE Medical</div></div>
<div class="abs search"><svg width="44" height="44" viewBox="0 0 44 44"><circle cx="20" cy="20" r="7" stroke="#fff" stroke-width="2.5" fill="none"/><path d="M25 25l6 6" stroke="#fff" stroke-width="2.5"/></svg></div>

<!-- hero -->
<section class="abs hero" role="img" aria-label="Pregnant woman in a grey sweater standing by a bright window with sheer curtains"></section>
<h1 class="abs hero-title">Feel Safe With Mom’s Care</h1>
<p class="abs hero-text">Lorem ipsum dolor sit amet, consectetuer adipiscing elit, sed diamest nonummy nibh euismod tincidunt ut laoreet dolore magna.</p>
<div class="abs dots"><span class="on"></span><span></span><span></span><span></span></div>

<!-- trimester -->
<h2 class="abs heading" style="top:740px">PREGNANCY <em>TRIMESTER</em></h2>
<svg class="abs divider" style="top:784px" width="40" height="16" viewBox="0 0 40 16"><path d="M0 12h40" stroke="#ccc"/><path d="M12 8h16" stroke="#5aac44" stroke-width="2"/><circle cx="20" cy="5" r="3" fill="#1d6fb8"/></svg>
<p class="abs intro" style="top:818px">Lorem Ipsum is simply dummy text of the printing and typesetting industry. Lorem Ipsum has been the industry's standard dummy text ever since the 1500s, when an unknown printer took a galley of type and scrambled it to make a type specimen book. It has survived not only five centuries, but also the leap into electronic typesetting, remaining essentially unchanged. It was popularised in the 1960s with the release .</p>

<div class="abs tri-photo" style="left:100px;background:linear-gradient(135deg,#8a8a8a,#c9b8a8 60%,#e2d6cc)" role="img" aria-label="Hands holding a pregnancy test"></div>
<div class="abs tri-photo" style="left:442px;background:linear-gradient(135deg,#f4f4f4,#9fd1cf 55%,#cfe6e2)" role="img" aria-label="Expectant mother beside a nursery crib with a teddy bear"></div>
<div class="abs tri-photo" style="left:785px;background:linear-gradient(135deg,#f5f5f5,#7a5640 50%,#efefef)" role="img" aria-label="Pregnant belly in a white top"></div>

<div class="abs tri-title" style="left:100px">FIRST TRIMESTER</div>
<div class="abs tri-title" style="left:442px">SECOND TRIMESTER</div>
<div class="abs tri-title" style="left:785px">THIRD TRIMESTER</div>
<div class="abs tri-btn btn" style="left:194px">Read More<span class="arr"><svg width="10" height="10" viewBox="0 0 10 10"><path d="M3 1l4 4-4 4" stroke="#1d6fb8" stroke-width="2" fill="none"/></svg></span></div>
<div class="abs tri-btn btn" style="left:536px">Read More<span class="arr"><svg width="10" height="10" viewBox="0 0 10 10"><path d="M3 1l4 4-4 4" stroke="#1d6fb8" stroke-width="2" fill="none"/></svg></span></div>
<div class="abs tri-btn btn" style="left:879px">Read More<span class="arr"><svg width="10" height="10" viewBox="0 0 10 10"><path d="M3 1l4 4-4 4" stroke="#1d6fb8" stroke-width="2" fill="none"/></svg></span></div>

<!-- fertility / basics band -->
<section class="abs band left" role="img" aria-label="Blue-toned photo of a mother and baby">
  <h3 style="left:100px">FERTILITY</h3>
  <p style="left:100px">Lorem Ipsum is simply dummy text of the printing and typesetting industry. Lorem Ipsum has been the industry's standard dummy text ever since the 1500s, when an unknown printer took a galley of type and scrambled it to make a type specimen book. It has survived not only five centuries, but also the leap into electronic typesetting.</p>
  <div class="btn ghost" style="left:100px">Read More<span class="arr"><svg width="10" height="10" viewBox="0 0 10 10"><path d="M3 1l4 4-4 4" stroke="#5aac44" stroke-width="2" fill="none"/></svg></span></div>
</section>
<section class="abs band right" role="img" aria-label="Green-toned photo of a mother with her child outdoors">
  <h3 style="left:140px">PREGNANCY BASICS</h3>
  <p style="left:140px">Lorem Ipsum is simply dummy text of the printing and typesetting industry. Lorem Ipsum has been the industry's standard dummy text ever since the 1500s, when an unknown printer took a galley of type and scrambled it to make a type specimen book. It has survived not only five centuries, but also the leap into electronic typesetting.</p>
  <div class="btn ghost" style="left:140px;background:var(--blue)">Read More<span class="arr"><svg width="10" height="10" viewBox="0 0 10 10"><path d="M3 1l4 4-4 4" stroke="#1d6fb8" stroke-width="2" fill="none"/></svg></span></div>
</section>
<div class="abs hub"><div class="brand"><div class="dot"></div><div class="name">KRE Medical</div></div></div>

<!-- articles -->
<h2 class="abs heading" style="top:1728px">OUR <em>ARTICLES</em></h2>
<svg class="abs divider" style="top:1772px" width="40" height="16" viewBox="0 0 40 16"><path d="M0 12h40" stroke="#ccc"/><path d="M12 8h16" stroke="#5aac44" stroke-width="2"/><circle cx="20" cy="5" r="3" fill="#1d6fb8"/></svg>
<p class="abs intro" style="top:1806px">Lorem Ipsum is simply dummy text of the printing and typesetting industry. Lorem Ipsum has been the industry's standard dummy text ever since the 1500s, when an unknown printer took a galley of type and scrambled it to make a type specimen book. It has survived not only five centuries.</p>

<div class="abs articles-bg"></div>
<svg class="abs chev" style="left:52px" width="16" height="28" viewBox="0 0 16 28"><path d="M13 2L3 14l10 12" stroke="#bbb" stroke-width="2" fill="none"/></svg>
<svg class="abs chev" style="left:1130px" width="16" height="28" viewBox="0 0 16 28"><path d="M3 2l10 12-10 12" stroke="#bbb" stroke-width="2" fill="none"/></svg>
<div class="abs thumb" style="left:100px;background:linear-gradient(135deg,#e9dfd7,#b99a85)" role="img" aria-label="Article photo: pregnant belly"></div>
<div class="abs thumb sel" style="left:244px;background:linear-gradient(135deg,#d9c5b6,#f3efea)" role="img" aria-label="Article photo: sleeping newborn"></div>
<div class="abs pin"></div>
<div class="abs thumb" style="left:420px;background:linear-gradient(135deg,#6fae5e,#e8f0e3)" role="img" aria-label="Article photo: mother outdoors"></div>
<div class="abs thumb" style="left:562px;background:linear-gradient(135deg,#f1e2d8,#d9a98e)" role="img" aria-label="Article photo: expectant mother resting"></div>
<div class="abs thumb" style="left:702px;background:linear-gradient(135deg,#e6dcd4,#a88a78)" role="img" aria-label="Article photo: hands on belly"></div>
<div class="abs thumb" style="left:842px;background:linear-gradient(135deg,#f0f0f0,#c9bbb2)" role="img" aria-label="Article photo: medical checkup"></div>
<div class="abs thumb" style="left:980px;background:linear-gradient(135deg,#3d8bd8,#c9a184)" role="img" aria-label="Article photo: pregnant woman in blue"></div>

<div class="abs art-photo" role="img" aria-label="Newborn baby wrapped in a white blanket"></div>
<div class="abs vline" style="top:2090px;height:20px"></div>
<div class="abs vline" style="top:2146px;height:14px"></div>
<div class="abs vline" style="top:2196px;height:142px"></div>
<div class="abs social-dot" style="top:2110px"></div>
<div class="abs social-dot" style="top:2160px"></div>
<div class="abs art">
  <h4>COMMON PREGNANCY CONCERNS</h4>
  <div class="meta">Friday, July 15, 2016 <span>|</span> by: Lorem Ipsum Dolor</div>
  <p>Lorem ipsum dolor sit amet, consectetuer adipiscing elit, sed diam nonummy nibh euismod tincidunt ut laoreet dolore magna aliquam erat volutpat. Ut wisi enim ad minim veniam, quis nostrud exerci tation ullamcorper mori suscipit lobortis nisl ut aliquip ex ea commodo consequat. Duis autem vel eum iriure dolor in hendrerit in vulpk utate velit esse molestie consequat, vel illum dolore eu feugiat nulla facilisis at vero eros et accumsan et iuston odio dignissim qui blandit praesent luptatum zzril delenit augue duis dolore te feugait nulla facilisi. Ut wisidoml enim ad minim veniam, quis nostrud exerci tation ullamcorper suscipit lobortis nisl ut aliquip ex ea commodomi more consequat. Lorem ipsum dolor sit amet, consectetuer adipiscing elit, sed diam nonummy nibh euismod.</p>
</div>

<!-- tips & news -->
<h3 class="abs col-head" style="left:100px">PREGNANCY <em>TIPS</em></h3>
<div class="abs navc" style="left:498px"><svg width="8" height="10" viewBox="0 0 8 10"><path d="M6 1L2 5l4 4" stroke="#888" stroke-width="2" fill="none"/></svg></div>
<div class="abs navc on" style="left:528px"><svg width="8" height="10" viewBox="0 0 8 10"><path d="M2 1l4 4-4 4" stroke="#1d6fb8" stroke-width="2" fill="none"/></svg></div>
<div class="abs col-rule" style="left:100px;width:456px"></div>
<div class="abs vsep"></div>
<h3 class="abs col-head" style="left:648px">LATEST <em>NEWS</em></h3>
<div class="abs navc" style="left:1044px"><svg width="8" height="10" viewBox="0 0 8 10"><path d="M6 1L2 5l4 4" stroke="#888" stroke-width="2" fill="none"/></svg></div>
<div class="abs navc on" style="left:1074px"><svg width="8" height="10" viewBox="0 0 8 10"><path d="M2 1l4 4-4 4" stroke="#1d6fb8" stroke-width="2" fill="none"/></svg></div>
<div class="abs col-rule" style="left:648px;width:452px"></div>

<div class="abs tip-photo" style="left:100px;top:2512px" role="img" aria-label="Doctor consulting with an expectant mother"></div>
<div class="abs" style="left:237px;top:2512px;width:320px">
  <div class="item-title">SED UT PERSPICIATIS UNDE OMNIS ISTE</div>
  <div class="item-text">Lorem Ipsum is simply dummy text of the printing and sedum typesetting industry n the industry's ...[+]</div>
  <div class="item-date" style="margin-top:8px">▦ February 12, 2017</div>
</div>
<div class="abs tip-photo" style="left:100px;top:2630px" role="img" aria-label="Expectant mother doing yoga"></div>
<div class="abs" style="left:237px;top:2630px;width:320px">
  <div class="item-title">SED UT PERSPICIATIS UNDE OMNIS ISTE</div>
  <div class="item-text">Lorem Ipsum is simply dummy text of the printing and sedum typesetting industry n the industry's ...[+]</div>
  <div class="item-date" style="margin-top:8px">▦ February 12, 2017</div>
</div>

<div class="abs datebox" style="left:648px;top:2512px"><div class="d">12</div><div class="m">FEB<br>2017</div></div>
<div class="abs" style="left:727px;top:2512px;width:372px">
  <div class="item-title">SED UT PERSPICIATIS UNDE OMNIS ISTE</div>
  <div class="item-text">Lorem Ipsum is simply dummy text of the printing and sedum typesetting industry n the Lorem Ipsum is simply dummy text of the printing and sedum the industry's ...[+]</div>
</div>
<div class="abs col-rule" style="left:727px;width:372px;top:2614px"></div>
<div class="abs datebox" style="left:648px;top:2636px"><div class="d">12</div><div class="m">FEB<br>2017</div></div>
<div class="abs" style="left:727px;top:2636px;width:372px">
  <div class="item-title">SED UT PERSPICIATIS UNDE OMNIS ISTE</div>
  <div class="item-text">Lorem Ipsum is simply dummy text of the printing and sedum typesetting industry n the Lorem Ipsum is simply dummy text of the printing and sedum the industry's ...[+]</div>
</div>

<!-- footer -->
<footer class="abs footer"></footer>
<div class="abs map" role="img" aria-label="Faint world map backdrop"></div>
<nav class="abs fnav">
  <a style="left:186px">Home</a><span class="sep" style="left:275px"></span>
  <a style="left:310px">Fertility</a><span class="sep" style="left:429px"></span>
  <a style="left:466px">Pregnancy Basics</a><span class="sep" style="left:670px"></span>
  <a style="left:703px">Articles</a><span class="sep" style="left:818px"></span>
  <a style="left:853px">Tips</a><span class="sep" style="left:924px"></span>
  <a style="left:962px">News</a>
</nav>
<div class="abs frule"></div>

<h4 class="abs fhead" style="left:100px">QUICK INQUIRY</h4>
<div class="abs field" style="top:2962px">Name</div>
<div class="abs field" style="top:3006px">Email</div>
<div class="abs field" style="top:3050px">Phone</div>
<div class="abs field msg" style="top:3094px">Message</div>
<div class="abs btn submit">SUBMIT<span class="arr"><svg width="10" height="10" viewBox="0 0 10 10"><path d="M3 1l4 4-4 4" stroke="#1d6fb8" stroke-width="2" fill="none"/></svg></span></div>

<div class="abs flogo"><div class="dot"></div><div class="name">KRE Medical</div></div>

<h4 class="abs fhead" style="left:778px">CONTACT DETAILS</h4>
<div class="abs fcontact" style="top:2962px">
  <div class="ic"><svg width="12" height="16" viewBox="0 0 12 16"><path d="M6 0a6 6 0 00-6 6c0 4.5 6 10 6 10s6-5.5 6-10a6 6 0 00-6-6z" fill="#fff"/><circle cx="6" cy="6" r="2" fill="#0f1a24"/></svg></div>
  <div class="t"><b>KRE MEDICAL</b>Lorem Ipsum is simply dummy text of the printing and typesetting industry.</div>
</div>
<div class="abs fcontact" style="top:3042px">
  <div class="ic"><svg width="14" height="11" viewBox="0 0 14 11"><rect x="0.5" y="0.5" width="13" height="10" fill="#fff"/><path d="M1 1l6 5 6-5" stroke="#0f1a24" fill="none"/></svg></div>
  <div class="t"><b>EMAIL</b>info@kremedical.com</div>
</div>
<div class="abs fcontact" style="top:3100px">
  <div class="ic"><svg width="14" height="14" viewBox="0 0 24 24"><path fill="#fff" d="M6.6 10.8a15 15 0 006.6 6.6l2.2-2.2c.3-.3.7-.4 1-.2 1.1.4 2.3.6 3.6.6.6 0 1 .4 1 1V20c0 .6-.4 1-1 1A17 17 0 013 4c0-.6.4-1 1-1h3.5c.6 0 1 .4 1 1 0 1.3.2 2.5.6 3.6.1.3 0 .7-.2 1z"/></svg></div>
  <div class="t"><b>CALL US</b>123 - 456 -7890</div>
</div>
<div class="abs sq" style="left:782px;background:#3b5998"></div>
<div class="abs sq" style="left:812px;background:#0077b5"></div>
<div class="abs sq" style="left:842px;background:#1da1f2"></div>
<div class="abs sq" style="left:872px;background:#dd4b39"></div>

<div class="abs copy">Copyright © 2016 KRE Medical. All Rights Reserved.</div>

</body>
</html>
```